Gilt Corner Shop Sign

Name of company
Gilt Corner
Gilt Corner is a picture framing shop and art gallery selling custom frames, art work and gifts.
Needing a design for shop front sign.

The Sign
The sign is above the shop front window and is approximately 12 feet wide by 43 inches high. White on black. White striped boarder that looks like a picture frame with Gilt Corner in classic lettering including space for a phone number and it may or may not need to include description of services. Something cute in one area like a picture frame with a heart inside. A friendly feel like something that would be special and feels like yours. I have attached a photo of the existing sign to be replaced.

Thank you for your time.

```html
<!DOCTYPE html>
<html lang="en">
<head>
<meta charset="utf-8">
<title>Gilt Corner Shop Sign</title>
<link rel="stylesheet" href="https://fonts.googleapis.com/css2?family=Abril+Fatface&family=Roboto+Condensed:wght@700&display=swap">
<style>
  :root {
    --backdrop: #e9e7e3;
    --sign-black: #000000;
    --sign-white: #ffffff;
    --pattern-tone: #bdbdbd;
    --flourish-tone: #6a6a6a;
  }
  html, body {
    margin: 0;
    padding: 0;
    width: 1200px;
    height: 1200px;
    overflow: hidden;
    background: var(--backdrop);
  }
  .canvas {
    position: relative;
    width: 1200px;
    height: 1200px;
  }
  .sign {
    position: absolute;
    left: 12px;
    top: 435px;
    width: 1176px;
    height: 330px;
    background: var(--sign-black);
  }
  .sign__border-pattern {
    position: absolute;
    inset: 0;
    width: 100%;
    height: 100%;
  }
  .sign__flourish {
    position: absolute;
    left: 393px;
    top: 50px;
    width: 390px;
    height: 58px;
    border-radius: 29px;
    background: radial-gradient(ellipse at center, var(--flourish-tone) 0%, rgba(106,106,106,0.35) 60%, rgba(0,0,0,0) 100%);
  }
  .sign__name {
    position: absolute;
    left: 0;
    right: 0;
    top: 92px;
    margin: 0;
    text-align: center;
    font-family: "Abril Fatface", "Playfair Display", serif;
    font-weight: 400;
    font-size: 150px;
    line-height: 1;
    color: var(--sign-white);
    letter-spacing: 1px;
  }
  .sign__rule {
    position: absolute;
    left: 50px;
    right: 50px;
    height: 1.5px;
    background: var(--sign-white);
  }
  .sign__rule--top { top: 246px; }
  .sign__rule--bottom { top: 287px; }
  .sign__contact {
    position: absolute;
    top: 252px;
    font-family: "Roboto Condensed", "Arial Narrow", sans-serif;
    font-weight: 700;
    font-size: 24px;
    line-height: 30px;
    letter-spacing: 1.5px;
    color: var(--sign-white);
  }
  .sign__web { left: 52px; }
  .sign__phone { right: 52px; }
</style>
</head>
<body>
<main class="canvas">
  <section class="sign">
    <svg class="sign__border-pattern" viewBox="0 0 1176 330" aria-hidden="true">
      <rect x="0" y="0" width="1176" height="330" fill="var(--sign-black)"/>
      <path role="img" aria-label="Decorative scalloped picture-frame border"
            fill="var(--pattern-tone)" fill-rule="evenodd"
            d="M2 2 H1174 V328 H2 Z M16 16 V314 H1160 V16 Z"/>
      <rect x="22" y="22" width="1132" height="286" fill="none" stroke="var(--sign-white)" stroke-width="2"/>
    </svg>
    <div class="sign__flourish" role="img" aria-label="Swirling line flourish with a small heart at its centre"></div>
    <h1 class="sign__name">Gilt Corner</h1>
    <div class="sign__rule sign__rule--top"></div>
    <div class="sign__contact sign__web">www.giltcornerstudio.com</div>
    <div class="sign__contact sign__phone">Phone : 5550192847</div>
    <div class="sign__rule sign__rule--bottom"></div>
  </section>
</main>
</body>
</html>
```